AUSTRALIAN CONSULTING FIRM BUSINESS CARD - MODERN

We are wanting a modern, clean lined business card design. We are professional niche consultancy firm situated in Australia called Harbrook Advisory Partners Pty Ltd.
The card should communicate professionalism and creativity and draw on our logo design (attached).
The design should be two sided, landscape orientation.
Target Market(s)
government, not for profit sector, corporate clients
Industry/Entity Type
Landscape
Requirements
Must have
- logo
no new introduced colours

```html
<!DOCTYPE html>
<html lang="en">
<head>
<meta charset="utf-8">
<title>Harbrook Advisory Partners – Business Card</title>
<link href="https://fonts.googleapis.com/css2?family=Open+Sans:wght@400;600;800&display=swap" rel="stylesheet">
<style>
  :root {
    --backdrop: #3b3b3d;
    --card: #ffffff;
    --navy: #1c1f7c;
    --purple: #a3248f;
    --teal: #1f9bc4;
    --lime: #8cc63f;
    --text-grey: #6d6d6d;
    --role-grey: #555555;
  }
  * { margin: 0; padding: 0; box-sizing: border-box; }
  html, body {
    width: 1200px; height: 900px; overflow: hidden;
    background: var(--backdrop);
    font-family: "Open Sans", Arial, sans-serif;
  }
  .canvas { position: relative; width: 1200px; height: 900px; }
  .card {
    position: absolute;
    width: 680px; height: 390px;
    background: var(--card);
    border-radius: 26px;
    overflow: hidden;
    box-shadow: 0 10px 30px rgba(0,0,0,0.35);
  }
  .card--front { left: 60px; top: 40px; }
  .card--back { right: 60px; top: 470px; }

  /* Front */
  .brand {
    position: absolute; left: 40px; top: 36px;
    display: flex; align-items: center; gap: 12px;
  }
  .brand__dot { width: 34px; height: 34px; border-radius: 50%; background: var(--teal); }
  .brand__name { font-weight: 800; font-size: 22px; color: var(--navy); }
  .address {
    position: absolute; left: 40px; top: 108px;
    font-size: 15px; line-height: 21px; color: var(--text-grey);
  }
  .contacts {
    position: absolute; left: 40px; top: 168px;
    list-style: none; font-size: 15px; line-height: 23px; color: var(--text-grey);
  }
  .contacts li { display: flex; align-items: center; gap: 9px; }
  .contacts svg { width: 13px; height: 13px; fill: var(--teal); flex: none; }
  .person { position: absolute; right: 60px; top: 222px; text-align: right; }
  .person__name { font-weight: 600; font-size: 24px; color: var(--teal); }
  .person__role { font-size: 15px; color: var(--role-grey); }
  .accent-band {
    position: absolute; left: 0; right: 0; bottom: 0; height: 52px;
    background: linear-gradient(90deg, var(--teal) 0%, var(--purple) 50%, var(--lime) 100%);
    opacity: 0.9;
  }

  /* Back */
  .back-brand {
    position: absolute; right: 44px; bottom: 70px;
    display: flex; align-items: center; gap: 14px;
  }
  .back-brand__dot { width: 46px; height: 46px; border-radius: 50%; background: var(--purple); }
  .back-brand__name {
    font-weight: 800; font-size: 26px; color: var(--navy); text-align: right; line-height: 1.15;
  }
</style>
</head>
<body>
<div class="canvas">

  <section class="card card--front" aria-label="Business card front">
    <div class="brand">
      <span class="brand__dot"></span>
      <span class="brand__name">Harbrook Advisory Partners Pty Ltd</span>
    </div>

    <p class="address">48 Kellerman Street, Suite 12<br>Carlton North, VIC 3054</p>

    <ul class="contacts">
      <li><svg viewBox="0 0 16 16"><path d="M3.5 1l3 3-1.8 1.8a9 9 0 0 0 5.5 5.5L12 9.5l3 3-2 2.5C6.5 15 1 9.5 1 3z"/></svg>03-9417-2286</li>
      <li><svg viewBox="0 0 16 16"><rect x="1" y="11" width="2.5" height="4"/><rect x="5" y="8" width="2.5" height="7"/><rect x="9" y="5" width="2.5" height="10"/><rect x="13" y="2" width="2.5" height="13"/></svg>03-9417-2286</li>
      <li><svg viewBox="0 0 16 16"><path d="M1 3h14v10H1z M2 4.5v.3l6 4 6-4v-.3z" fill-rule="evenodd"/></svg>info@harbrook.com</li>
      <li><svg viewBox="0 0 16 16"><circle cx="8" cy="8" r="7"/></svg>www.harbrook.com</li>
    </ul>

    <div class="person">
      <p class="person__name">Daniel Marsh</p>
      <p class="person__role">Vice President</p>
    </div>

    <div class="accent-band" role="img" aria-label="Decorative colour band in blue, purple and green"></div>
  </section>

  <section class="card card--back" aria-label="Business card back">
    <div class="back-brand">
      <span class="back-brand__dot"></span>
      <span class="back-brand__name">Harbrook Advisory<br>Partners Pty Ltd</span>
    </div>
  </section>

</div>
</body>
</html>
```